web site for Biblical Oils, Candles and Perfumes

To make a web design with "magento".
To show image of the company/products and to be a shop.
see sample:
www.morvatlu.ws
it is important that we will have pages of description of the products category
then puctures with item description and option to select how many to add to the cart.
Special reduction on product or full category.
Managing clients with possibility to give special reduction to specific client.
each product can be see in bigger image.
can write more information about the product.

Target Market(s)

christian, evangelist, bible lover, belivers

Industry/Entity Type

It Company

Number of Pages Required

5+ page

Requirements
Must have
• my possibility to maintains the web-site by myself (wordpree workers)
Nice to have
• to have statitics

```html
<!DOCTYPE html>
<html lang="en">
<head>
<meta charset="utf-8">
<title>Morvatlu – Biblical Oils, Candles and Perfumes</title>
<link rel="stylesheet" href="https://fonts.googleapis.com/css2?family=Open+Sans:wght@400;600;700;800&family=Montserrat:wght@500;700;800&display=swap">
<style>
:root{
  --blue:#1d5ea8;
  --blue-dark:#15477f;
  --blue-side:#2a6db6;
  --ink:#333a44;
  --muted:#8a919a;
  --line:#e3e6ea;
  --red:#c8412f;
  --gold:#e2b33a;
  --bg:#ffffff;
  --soft:#f4f6f8;
  --footer:#f7f8f9;
}
*{box-sizing:border-box;margin:0;padding:0}
html,body{width:1200px;height:2476px;overflow:hidden}
body{background:var(--bg);font-family:"Open Sans",Arial,sans-serif;color:var(--ink);font-size:13px;position:relative}
a{color:inherit;text-decoration:none}
.wrap{position:absolute;left:80px;width:1040px}

/* top bar */
.topbar{position:absolute;top:0;left:0;width:1200px;height:30px;border-bottom:1px solid var(--line);font-size:11px;color:var(--muted)}
.topbar .wrap{top:0;height:30px;display:flex;justify-content:space-between;align-items:center}
.topbar ul{display:flex;gap:26px;list-style:none}
.topbar li::before{content:"";display:inline-block;width:6px;height:6px;border-radius:50%;background:var(--blue);margin-right:6px;vertical-align:middle}

/* header */
.header .wrap{top:30px;height:90px;display:flex;align-items:center;justify-content:space-between}
.brand{display:flex;align-items:center;gap:10px;font-weight:700;font-size:26px;color:var(--blue)}
.brand .dot{width:22px;height:22px;border-radius:50%;background:var(--blue)}
.search{display:flex;width:480px;height:34px;border:1px solid var(--line);border-radius:3px;overflow:hidden}
.search .field{flex:1;padding:0 12px;line-height:32px;color:var(--muted);font-size:12px}
.search .cat{width:110px;background:var(--soft);border-left:1px solid var(--line);line-height:32px;text-align:center;font-size:12px}
.search .go{width:44px;background:var(--blue);display:flex;align-items:center;justify-content:center}
.cart{display:flex;align-items:center;gap:8px;font-size:12px;color:var(--muted)}

/* nav */
.nav{position:absolute;top:122px;left:0;width:1200px;height:34px;background:var(--blue)}
.nav .wrap{top:0;height:34px;display:flex}
.nav .products{width:240px;background:var(--blue-dark);color:#fff;font-weight:700;font-size:13px;line-height:34px;padding-left:16px;letter-spacing:.5px}
.nav .products span{display:inline-block;width:14px;border-top:2px solid #fff;border-bottom:2px solid #fff;height:10px;margin-right:10px;vertical-align:middle}
.nav ul{display:flex;list-style:none;margin-left:36px}
.nav li{color:#fff;font-weight:700;font-size:12px;line-height:34px;width:130px;letter-spacing:.5px}

/* hero */
.hero{top:156px;height:440px;display:flex}
.sidebar{width:240px;background:var(--blue-side);list-style:none;padding-top:6px}
.sidebar li{color:#fff;font-size:12px;height:40px;line-height:40px;padding-left:24px;border-bottom:1px solid rgba(255,255,255,.15);position:relative}
.sidebar li::before{content:"";position:absolute;left:12px;top:18px;width:4px;height:4px;border-radius:50%;background:#fff}
.hero-visual{flex:1;position:relative;background:linear-gradient(100deg,#e4eaef 0%,#eef1f3 45%,#cdd9e3 100%)}
.hero-copy{position:absolute;left:150px;top:318px;text-align:center;width:500px}
.hero-copy .lead{font-family:"Montserrat",sans-serif;font-weight:500;font-size:21px;color:var(--blue)}
.hero-copy .big{font-family:"Montserrat",sans-serif;font-weight:800;font-size:25px;color:var(--ink);margin-top:4px}
.dots{position:absolute;bottom:14px;left:50%;display:flex;gap:6px;transform:translateX(-50%)}
.dots i{width:8px;height:8px;border-radius:50%;background:#fff;opacity:.8}
.dots i:first-child{background:var(--blue);opacity:1}

/* banners */
.promo{position:absolute;top:610px;height:160px;padding:18px}
.promo h3{font-family:"Montserrat",sans-serif;font-weight:800;font-size:18px;line-height:1.1}
.promo .btn{display:inline-block;margin-top:12px;padding:4px 14px;border:1px solid currentColor;font-size:10px;font-weight:700}
.promo.perfume{left:80px;width:250px;background:linear-gradient(90deg,#c48a2f,#e6be6a 60%,#d9a54a);color:#7a3e0c}
.promo.olive{left:340px;width:250px;background:linear-gradient(90deg,#8fa447,#c8d07a 60%,#9db152);color:#3f4d12}
.promo.model{left:600px;width:520px;height:440px;background:linear-gradient(110deg,#f1ebe2 0%,#e7d8c4 50%,#caa887 100%);color:#6f5a1f}
.promo.model h3{position:absolute;right:40px;top:290px;text-align:right;font-size:26px}
.promo.model .btn{position:absolute;right:40px;top:362px}

/* special offer */
.special{position:absolute;left:80px;top:790px;width:500px;height:260px;border:1px solid var(--line);display:flex;padding:28px 20px}
.special .thumb{width:150px;height:150px;background:linear-gradient(160deg,#1e3f86,#3a63b0 55%,#c7cfe0);margin-right:24px}
.special h2{font-family:"Montserrat",sans-serif;font-size:15px;font-weight:700;color:var(--blue);margin-bottom:14px}
.special .info{flex:1}
.row{display:flex;justify-content:space-between;align-items:center}
.pname{font-size:10px;font-weight:700;color:var(--ink);text-transform:uppercase}
.price{color:var(--red);font-weight:700;font-size:13px}
.stars{color:var(--gold);font-size:12px;letter-spacing:1px;margin:4px 0}
.desc{font-size:10px;color:var(--muted);line-height:1.5}
.sm-btn{display:inline-block;border:1px solid var(--line);font-size:9px;color:var(--muted);padding:3px 10px;margin-top:10px}

/* featured */
.tabs{position:absolute;left:80px;top:1110px;width:1040px;display:flex;align-items:center;gap:18px;border-bottom:1px solid var(--line);padding-bottom:10px}
.tabs b{font-family:"Montserrat",sans-serif;color:var(--blue);font-size:15px}
.tabs span{font-family:"Montserrat",sans-serif;color:var(--muted);font-size:15px}
.tabs .arrows{margin-left:auto;display:flex;gap:6px}
.tabs .arrows i{width:22px;height:22px;border-radius:50%;border:1px solid var(--line);display:flex;align-items:center;justify-content:center;font-style:normal;font-size:11px;color:var(--muted)}
.grid{position:absolute;left:80px;top:1170px;width:1040px;display:flex;gap:20px}
.card{width:245px;height:300px;border:1px solid var(--line);text-align:center;padding:16px}
.card .thumb{height:160px;margin-bottom:14px;background:linear-gradient(180deg,#f5f5f2,#e6dfc7)}
.card .desc{margin:3px 0}

/* top sellers + about */
.sec-title{font-family:"Montserrat",sans-serif;color:var(--blue);font-weight:700;font-size:15px;padding-bottom:8px;border-bottom:1px solid var(--line)}
.sellers{position:absolute;left:80px;top:1580px;width:480px}
.sellers .items{display:grid;grid-template-columns:1fr 1fr;gap:24px 20px;margin-top:24px}
.item{display:flex;gap:12px;align-items:center}
.item .thumb{width:90px;height:80px;flex:none;background:linear-gradient(180deg,#f4f1e6,#d9c79a)}
.about{position:absolute;left:600px;top:1580px;width:520px}
.about p{font-size:11px;color:var(--muted);line-height:1.6;margin-top:12px}
.about h4{font-size:10px;font-weight:700;margin-top:14px}
.about strong{color:var(--ink)}

/* features band */
.band{position:absolute;top:2010px;left:0;width:1200px;height:150px;background:var(--blue)}
.band .wrap{top:0;height:150px;display:flex;justify-content:space-around;align-items:center}
.feat{text-align:center;color:#fff;width:220px}
.feat svg{display:block;margin:0 auto 10px}
.feat b{display:block;font-family:"Montserrat",sans-serif;font-size:14px;letter-spacing:.5px}
.feat small{font-size:10px;opacity:.8}

/* footer */
.footer{position:absolute;top:2160px;left:0;width:1200px;height:316px;background:var(--footer)}
.footer .wrap{top:36px;display:flex;gap:30px}
.col{width:180px}
.col h5{font-family:"Montserrat",sans-serif;font-size:13px;font-weight:700;color:var(--blue);margin-bottom:16px}
.col ul{list-style:none}
.col li{font-size:11px;color:var(--muted);line-height:22px}
.contact li{display:flex;gap:8px;align-items:flex-start;line-height:18px;margin-bottom:10px}
.news{width:260px}
.news .form{display:flex;height:30px;border:1px solid var(--line);background:#fff}
.news .form span{flex:1;font-size:11px;color:var(--muted);line-height:28px;padding-left:10px}
.news .form i{width:60px;background:var(--blue)}
.social{display:flex;gap:8px;margin-top:10px}
.social i{width:26px;height:26px;border-radius:50%;background:var(--blue)}
.pay{display:flex;gap:6px;margin-top:20px}
.pay i{width:34px;height:20px;background:#d4d8de;border-radius:2px}
.copy{position:absolute;left:80px;top:274px;font-size:10px;color:var(--muted)}
</style>
</head>
<body>

<div class="topbar">
  <div class="wrap">
    <ul><li>Welcome visitor</li><li>Shipping Rates</li></ul>
    <ul><li>English</li><li>USD</li><li>My Account</li><li>My Wishlist</li><li>Checkout</li><li>Login</li></ul>
  </div>
</div>

<header class="header">
  <div class="wrap">
    <div class="brand"><span class="dot"></span>Morvatlu</div>
    <div class="search">
      <div class="field">Search</div>
      <div class="cat">Category ▾</div>
      <div class="go"><svg width="16" height="16" viewBox="0 0 16 16"><circle cx="7" cy="7" r="5" fill="none" stroke="#fff" stroke-width="2"/><line x1="11" y1="11" x2="15" y2="15" stroke="#fff" stroke-width="2"/></svg></div>
    </div>
    <div class="cart"><svg width="26" height="24" viewBox="0 0 26 24"><path d="M2 3h4l3 12h12l3-9H8" fill="none" stroke="#1d5ea8" stroke-width="2"/><circle cx="11" cy="20" r="2" fill="#1d5ea8"/><circle cx="20" cy="20" r="2" fill="#1d5ea8"/></svg>0 item(s)</div>
  </div>
</header>

<nav class="nav">
  <div class="wrap">
    <div class="products"><span></span>PRODUCTS</div>
    <ul><li>HOME</li><li>ABOUT</li><li>FAQ</li><li>HELP</li><li>CONTACT</li></ul>
  </div>
</nav>

<section class="wrap hero">
  <ul class="sidebar">
    <li>Anointing Oils</li><li>Biblical Perfumes</li><li>Dead Sea Cosmetic Skin Care</li><li>Dead Sea Home Spa</li><li>Olive Oil Soaps</li><li>Holy Land Gift Packs</li><li>Shofars</li><li>Special Offer</li>
  </ul>
  <div class="hero-visual" role="img" aria-label="Spa cosmetics banner photo: model wearing a white clay face mask">
    <div class="hero-copy">
      <div class="lead">Our Cosmetics &amp; Spa Products Are Rich in</div>
      <div class="big">VITAMINS &amp; DEAD SEA MINERALS</div>
    </div>
    <div class="dots"><i></i><i></i><i></i></div>
  </div>
</section>

<div class="promo perfume" role="img" aria-label="Golden perfume bottles on amber background">
  <h3>BIBLICAL<br>PERFUMES</h3><span class="btn">SHOP NOW</span>
</div>
<div class="promo olive" role="img" aria-label="Olive oil soap bars with olive branches">
  <h3>OLIVE OIL<br>SOAPS</h3><span class="btn">SHOP NOW</span>
</div>
<div class="promo model" role="img" aria-label="Model holding olive oil soap">
  <h3>OLIVE OIL<br>SOAPS</h3><span class="btn">SHOP NOW</span>
</div>

<section class="special">
  <div class="thumb" role="img" aria-label="Blue cosmetic jar with box"></div>
  <div class="info">
    <h2>SPECIAL OFFER</h2>
    <div class="row"><span class="pname">Lamp of Galilee</span><span class="price">$35.10</span></div>
    <div class="desc">Anointing Oil 30 ml</div>
    <div class="stars">★★★★★</div>
    <p class="desc">Pure oil blended with fragrant spices from the Holy Land. Made in small batches, bottled by hand and sealed for freshness. Ideal for prayer, blessing and a cherished gift.</p>
    <span class="sm-btn">ADD TO CART</span>
  </div>
</section>

<div class="tabs"><b>FEATURED</b><span>|</span><span>NEW</span><div class="arrows"><i>‹</i><i>›</i></div></div>
<section class="grid">
  <div class="card"><div class="thumb" role="img" aria-label="Anointing oil bottle with box"></div><div class="pname">Lamp of Galilee</div><div class="desc">Anointing Oil 30 ml</div><div class="price">$35.10</div><span class="sm-btn">ADD TO CART</span></div>
  <div class="card"><div class="thumb" role="img" aria-label="Anointing oil bottle with green box"></div><div class="pname">Lamp of Galilee</div><div class="desc">Anointing Oil 30 ml</div><div class="price">$40.12</div><span class="sm-btn">ADD TO CART</span></div>
  <div class="card"><div class="thumb" role="img" aria-label="Anointing oil bottle with gold box"></div><div class="pname">Lamp of Galilee</div><div class="desc">Anointing Oil 30 ml</div><div class="price">$55.10</div><span class="sm-btn">ADD TO CART</span></div>
  <div class="card"><div class="thumb" role="img" aria-label="Anointing oil bottle with blue box"></div><div class="pname">Lamp of Galilee</div><div class="desc">Anointing Oil 30 ml</div><div class="price">$20.60</div><span class="sm-btn">ADD TO CART</span></div>
</section>

<section class="sellers">
  <div class="sec-title">TOP SELLERS</div>
  <div class="items">
    <div class="item"><div class="thumb" role="img" aria-label="Anointing oil gift box"></div><div><div class="pname">Lamp of Galilee</div><div class="desc">Anointing Oil 30 ml</div><div class="price">$35.60</div></div></div>
    <div class="item"><div class="thumb" role="img" aria-label="Anointing oil bottle"></div><div><div class="pname">Lamp of Galilee</div><div class="desc">Anointing Oil 30 ml</div><div class="price">$40.10</div></div></div>
    <div class="item"><div class="thumb" role="img" aria-label="Perfume oil bottle"></div><div><div class="pname">Valley Bloom</div><div class="desc">Perfume Oil 10 ml</div><div class="price">$70.00</div></div></div>
    <div class="item"><div class="thumb" role="img" aria-label="Night cream jar"></div><div><div class="pname">Dead Sea Mineral Night Cream</div><div class="desc">Skin Care 50 ml</div><div class="price">$35.60</div></div></div>
  </div>
</section>

<section class="about">
  <div class="sec-title">A LITTLE ABOUT US</div>
  <p>Morvatlu specializes in the production and development of Dead Sea cosmetics and spa, anointing oils, biblical perfumes, candles, shofars and holy land gift packs.</p>
  <h4>DEAD SEA MINERAL COSMETICS &amp; SPA</h4>
  <p>Our own manufacturing of premium Dead Sea mineral products.</p>
  <p><strong>SKIN CARE:</strong> Day creams, night creams, eye creams, body lotions, protective moisturizers, mud masks, deep cleanser, hand creams, foot creams, body and bath oils and more.</p>
</section>

<section class="band">
  <div class="wrap">
    <div class="feat"><svg width="36" height="28" viewBox="0 0 36 28"><rect x="1" y="5" width="20" height="15" fill="none" stroke="#fff" stroke-width="2"/><path d="M21 10h8l5 5v5h-13z" fill="none" stroke="#fff" stroke-width="2"/><circle cx="8" cy="23" r="3" fill="#fff"/><circle cx="28" cy="23" r="3" fill="#fff"/></svg><b>FREE SHIPPING</b><small>On orders over $99</small></div>
    <div class="feat"><svg width="32" height="28" viewBox="0 0 32 28"><rect x="2" y="10" width="28" height="16" fill="none" stroke="#fff" stroke-width="2"/><rect x="0" y="6" width="32" height="5" fill="#fff"/><line x1="16" y1="6" x2="16" y2="26" stroke="#fff" stroke-width="2"/></svg><b>SPECIAL GIFT CARDS</b><small>On order over $99</small></div>
    <div class="feat"><svg width="30" height="30" viewBox="0 0 30 30"><path d="M8 2l5 6-3 3c2 4 5 7 9 9l3-3 6 5-3 5C14 27 3 16 2 5z" fill="#fff"/></svg><b>24/7 CUSTOMER CARE</b><small>+1 555 014 2290</small></div>
    <div class="feat"><svg width="30" height="30" viewBox="0 0 30 30"><circle cx="15" cy="15" r="13" fill="none" stroke="#fff" stroke-width="2"/><text x="15" y="21" text-anchor="middle" fill="#fff" font-size="16" font-weight="700" font-family="Open Sans,sans-serif">?</text></svg><b>HELP</b><small>Find quick answers</small></div>
  </div>
</section>

<footer class="footer">
  <div class="wrap">
    <div class="col contact" style="width:200px">
      <h5>CONTACT US</h5>
      <ul>
        <li><svg width="10" height="14" viewBox="0 0 10 14"><path d="M5 0a5 5 0 015 5c0 4-5 9-5 9S0 9 0 5a5 5 0 015-5z" fill="#1d5ea8"/></svg>2334 – North Quarter Street, Cedar Vale, NY 10012</li>
        <li><svg width="12" height="10" viewBox="0 0 12 10"><rect width="12" height="10" fill="#1d5ea8"/></svg>support@morvatlu.ws<br>www.morvatlu.ws</li>
        <li><svg width="12" height="12" viewBox="0 0 30 30"><path d="M8 2l5 6-3 3c2 4 5 7 9 9l3-3 6 5-3 5C14 27 3 16 2 5z" fill="#1d5ea8"/></svg>+1 555 014 2290</li>
      </ul>
    </div>
    <div class="col"><h5>INFORMATION</h5><ul><li>My account</li><li>Order history</li><li>Wish list</li><li>Warranty</li><li>Privacy Policy</li><li>Site map</li></ul></div>
    <div class="col"><h5>OUR OFFERS</h5><ul><li>New collection</li><li>Best sellers</li><li>Manufacturers</li><li>New products</li><li>Suppliers</li><li>Delivery &amp; returns</li></ul></div>
    <div class="col"><h5>OUR POLICY</h5><ul><li>Help &amp; Contact</li><li>Shipping &amp; Taxes</li><li>Return policy</li><li>Careers</li><li>Affiliates</li><li>Legal notice</li></ul></div>
    <div class="col news">
      <h5>GET NEWSLETTERS</h5>
      <div class="form"><span>Enter your email</span><i></i></div>
      <h5 style="margin-top:22px">CONNECT US</h5>
      <div class="social"><i></i><i></i><i></i><i></i></div>
      <div class="pay"><i></i><i></i><i></i><i></i><i></i></div>
    </div>
  </div>
  <div class="copy">© 2015 Morvatlu. All Rights Reserved.</div>
</footer>

</body>
</html>
```